Bahamas Pharmacy Requires Orbit Meds Flyer Re-Design

Hello,
We were so happy with your previous design we were hoping you'd be able to repair another design we had done. It's a half-letter single sided flyer (5.5 x 8) that promotes Orbit Medications. The information on the first side of the attached PDF is unnecessary except for the "Are you taking more than 3 medications a day?" On the interior of the attached PDF, we'd like to keep as much information as possible. A diagram similar to the one at the top is necessary to make it easy to read. We trust your design style and are excited to see what you can bring. Please use the Brightwater Vale Pharmacy Logo, Chirply, and Friendwall icons as you did on the "Sunrise Stroll Guide."
Updates
Reason: We would like to give participating designers more time to make changes to their designs.
Target Market(s)
Mixed Race and African American families with elderly family members
Industry/Entity Type
Pharmacy
Requirements
Must have
- Any persons used should have a diverse range of backgrounds, preferably mixed race as most persons in the Bahamas are. They and their loved ones should be happy and relieved that they no longer need to worry about their medicines. If any couples are used they should be older and either mixed or african american.
Nice to have
- It's nice to have the diagram that explains what the "orbit meds" program does.
Should not have
- Too many fonts, colors or serif fonts.

```html
<!DOCTYPE html>
<html lang="en">
<head>
<meta charset="utf-8">
<title>Brightwater Vale Pharmacy – Orbit Medications Flyer</title>
<link href="https://fonts.googleapis.com/css2?family=Arimo:wght@400;700&display=swap" rel="stylesheet">
<style>
  :root{
    --green:#6dbe45;
    --green-text:#6abf3f;
    --red:#c4202a;
    --red-dark:#a8161f;
    --ink:#333333;
    --brown:#3b2a1c;
    --paper:#ffffff;
    --stage:#e6e9e6;
  }
  *{margin:0;padding:0;box-sizing:border-box}
  html,body{width:1200px;height:1117px;overflow:hidden}
  body{background:var(--stage);font-family:"Arimo",Arial,sans-serif;color:var(--ink);position:relative}

  .flyer{position:absolute;left:272px;top:82px;width:655px;height:953px;background:var(--paper);overflow:hidden;box-shadow:0 10px 24px rgba(0,0,0,.25)}

  .hero-photo{position:absolute;left:0;top:0;width:655px;height:310px;
    background:linear-gradient(100deg,#d98a7a 0%,#e9c7b0 35%,#8fb2c8 60%,#b9a08a 80%,#5fc2c0 100%)}

  .brand-bar{position:absolute;left:0;top:310px;width:655px;height:86px}
  .brand{position:absolute;left:0;top:0;width:443px;height:86px;background:#fff}
  .brand-mark{position:absolute;left:22px;top:16px;width:44px;height:44px;background:var(--red)}
  .brand-name{position:absolute;left:114px;top:30px;font-size:21px;font-weight:400;color:var(--red);white-space:nowrap}
  .brand-rule{position:absolute;left:114px;top:57px;width:296px;height:3px;background:#555;border-radius:2px}
  .brand-tag{position:absolute;left:150px;top:66px;font-size:11.5px;color:#3c8a2e}
  .social{position:absolute;left:443px;top:0;width:212px;height:86px;background:var(--green)}
  .social-item{position:absolute;top:22px;display:flex;align-items:center;gap:5px;font-size:13px;font-weight:700;color:#fff}
  .social-item .sq{width:14px;height:14px;background:var(--red)}
  .social-chirply{left:40px}
  .social-friendwall{left:116px}

  .top-band{position:absolute;left:0;top:396px;width:655px;height:22px;background:var(--red)}

  .headline{position:absolute;left:0;top:444px;width:655px;text-align:center;font-size:19.5px;font-weight:700;color:var(--green-text);letter-spacing:.2px}

  .diagram{position:absolute;left:0;top:480px;width:655px;height:185px}
  .diagram svg{display:block}

  .program-title{position:absolute;left:21px;top:658px;font-size:21px;font-weight:700;color:var(--green-text)}
  .program-intro{position:absolute;left:21px;top:686px;font-size:13px;line-height:16px;color:var(--ink)}

  .benefits{position:absolute;left:24px;top:752px;width:320px;list-style:none}
  .benefits li{position:relative;padding-left:24px;font-size:10.6px;line-height:11.5px;margin-bottom:5.2px;color:var(--ink)}
  .benefits li.gap{margin-top:10px}
  .benefits svg{position:absolute;left:0;top:-1px}

  .contact{position:absolute;left:445px;top:682px;width:210px;height:221px;background:var(--green);color:var(--brown)}
  .contact h2{position:absolute;left:13px;top:22px;font-size:19.5px;font-weight:700;color:var(--brown)}
  .contact-address{position:absolute;left:46px;top:63px;font-size:12px;line-height:15px;color:var(--ink)}
  .contact-line{position:absolute;left:14px;display:flex;align-items:center;gap:9px;font-size:12px;color:var(--ink)}
  .contact .pin{position:absolute;left:16px;top:84px}

  .foot-line{position:absolute;left:0;top:927px;width:655px;height:3px;background:var(--green)}
  .foot-band{position:absolute;left:0;top:931px;width:655px;height:22px;background:var(--red)}
</style>
</head>
<body>
<main class="flyer">
  <div class="hero-photo" role="img" aria-label="Photo of a smiling multi-generation family sitting together on a sofa"></div>

  <header class="brand-bar">
    <div class="brand">
      <span class="brand-mark"></span>
      <span class="brand-name">Brightwater Vale Pharmacy</span>
      <span class="brand-rule"></span>
      <span class="brand-tag">Healthier choices, Lower Prices</span>
    </div>
    <div class="social">
      <span class="social-item social-chirply"><span class="sq"></span>Chirply</span>
      <span class="social-item social-friendwall"><span class="sq"></span>Friendwall</span>
    </div>
  </header>

  <div class="top-band"></div>

  <h1 class="headline">"ARE YOU TAKING MORE THAN 3 MEDICATIONS A DAY?"</h1>

  <section class="diagram">
    <svg width="655" height="185" viewBox="0 0 655 185">
      <rect x="0" y="53" width="655" height="82" fill="#c4202a"/>
      <path d="M190 30 C215 8 255 5 275 30" fill="none" stroke="#c4202a" stroke-width="6" stroke-linecap="round"/>
      <polygon points="265,22 284,40 285,16" fill="#c4202a"/>
      <path d="M370 160 C395 180 430 178 448 150" fill="none" stroke="#c4202a" stroke-width="6" stroke-linecap="round"/>
      <polygon points="438,150 458,140 452,162" fill="#c4202a"/>
      <g stroke="#dddddd" stroke-width="2">
        <circle cx="150" cy="93" r="64" fill="#5a82c4" role="img" aria-label="Photo of a weekly pill organiser tray"/>
        <circle cx="328" cy="93" r="64" fill="#efe6e4" role="img" aria-label="Photo of a hand taking a sealed medication pouch"/>
        <circle cx="505" cy="93" r="64" fill="#ecebe6" role="img" aria-label="Photo of a labelled pouch with assorted pills"/>
      </g>
    </svg>
  </section>

  <h2 class="program-title">ORBIT MEDICATIONS</h2>
  <p class="program-intro">Orbit Medication is easy and convenient.<br>Your enrollment simplifies all your medications<br>in one convenient packaging:</p>

  <ul class="benefits">
    <li><svg width="15" height="13" viewBox="0 0 15 13"><rect x="1" y="3" width="9" height="9" fill="none" stroke="#c4202a" stroke-width="1.6"/><path d="M3 7 L6 10 L14 1" fill="none" stroke="#c4202a" stroke-width="2.2"/></svg>No need to call in prescription refills.</li>
    <li><svg width="15" height="13" viewBox="0 0 15 13"><rect x="1" y="3" width="9" height="9" fill="none" stroke="#c4202a" stroke-width="1.6"/><path d="M3 7 L6 10 L14 1" fill="none" stroke="#c4202a" stroke-width="2.2"/></svg>Fewer trips to the pharmacy.</li>
    <li><svg width="15" height="13" viewBox="0 0 15 13"><rect x="1" y="3" width="9" height="9" fill="none" stroke="#c4202a" stroke-width="1.6"/><path d="M3 7 L6 10 L14 1" fill="none" stroke="#c4202a" stroke-width="2.2"/></svg>No worries about running out of your medication.</li>
    <li><svg width="15" height="13" viewBox="0 0 15 13"><rect x="1" y="3" width="9" height="9" fill="none" stroke="#c4202a" stroke-width="1.6"/><path d="M3 7 L6 10 L14 1" fill="none" stroke="#c4202a" stroke-width="2.2"/></svg>Prescription ready on your refill date.</li>
    <li><svg width="15" height="13" viewBox="0 0 15 13"><rect x="1" y="3" width="9" height="9" fill="none" stroke="#c4202a" stroke-width="1.6"/><path d="M3 7 L6 10 L14 1" fill="none" stroke="#c4202a" stroke-width="2.2"/></svg>All your daily medications organized by time of day.</li>
    <li><svg width="15" height="13" viewBox="0 0 15 13"><rect x="1" y="3" width="9" height="9" fill="none" stroke="#c4202a" stroke-width="1.6"/><path d="M3 7 L6 10 L14 1" fill="none" stroke="#c4202a" stroke-width="2.2"/></svg>Correct dose always at your fingertips.</li>
    <li class="gap"><svg width="15" height="13" viewBox="0 0 15 13"><rect x="1" y="3" width="9" height="9" fill="none" stroke="#c4202a" stroke-width="1.6"/><path d="M3 7 L6 10 L14 1" fill="none" stroke="#c4202a" stroke-width="2.2"/></svg>Convenient dose reminder system to get the best results possible from your madications.</li>
    <li class="gap"><svg width="15" height="13" viewBox="0 0 15 13"><rect x="1" y="3" width="9" height="9" fill="none" stroke="#c4202a" stroke-width="1.6"/><path d="M3 7 L6 10 L14 1" fill="none" stroke="#c4202a" stroke-width="2.2"/></svg>One week prior to your prescriptions being refilled we call you to verify what is needed.</li>
  </ul>

  <aside class="contact">
    <h2>CONTACT US</h2>
    <svg class="pin" width="20" height="28" viewBox="0 0 20 28"><path d="M10 0 C4.5 0 0 4.5 0 10 C0 17 10 28 10 28 C10 28 20 17 20 10 C20 4.5 15.5 0 10 0 Z" fill="#c4202a"/><circle cx="10" cy="10" r="4" fill="#6dbe45"/></svg>
    <p class="contact-address">14 Coral Crescent<br>Palmgate Plaza, Seabright,<br>Grand Bahama, Bahamas<br>Grand Bahama, Bahamas ,<br>SB 20417</p>
    <p class="contact-line" style="top:163px">
      <svg width="24" height="18" viewBox="0 0 24 18"><path d="M1 6 C1 1 23 1 23 6 L18 7 L17 4 L7 4 L6 7 Z" fill="#c4202a"/><rect x="4" y="8" width="16" height="9" rx="2" fill="#c4202a"/><circle cx="12" cy="12.5" r="2.5" fill="#6dbe45"/></svg>242-555-0142</p>
    <p class="contact-line" style="top:192px">
      <svg width="24" height="20" viewBox="0 0 24 20"><rect x="6" y="0" width="12" height="7" fill="#c4202a"/><rect x="1" y="7" width="22" height="12" rx="2" fill="#c4202a"/><rect x="5" y="10" width="9" height="2" fill="#6dbe45"/><rect x="5" y="14" width="9" height="2" fill="#6dbe45"/></svg>242-555-0198</p>
  </aside>

  <div class="foot-line"></div>
  <div class="foot-band"></div>
</main>
</body>
</html>
```